Kinward Harbor Center
Stationary and Business Cards
Kinward Harbor Center -
Creative Brief
Bright & Fun-filled
Marisol Thackery
48 Alder Lane Morristown, NJ 07931
marisol.thackery@alderlanehub.org
www.alderlanehub.org

```html
<!DOCTYPE html>
<html lang="en">
<head>
<meta charset="utf-8">
<title>Kinward Harbor Center — Stationery Set</title>
<link rel="stylesheet" href="https://fonts.googleapis.com/css2?family=Open+Sans:wght@400;600;700&display=swap">
<style>
  :root {
    --backdrop: #a5a7aa;
    --paper: #ffffff;
    --brand-blue: #2a6db5;
    --brand-blue-deep: #1b4f8f;
    --brand-blue-light: #5d9bd8;
    --accent-orange: #f0962a;
    --ink: #3b3b3b;
    --ink-soft: #6a6a6a;
  }
  * { margin: 0; padding: 0; box-sizing: border-box; }
  html, body { width: 1200px; height: 626px; overflow: hidden; }
  body {
    background: var(--backdrop);
    font-family: "Open Sans", Arial, sans-serif;
    color: var(--ink);
    position: relative;
  }
  .piece {
    position: absolute;
    background: var(--paper);
    overflow: hidden;
    box-shadow: 0 1px 3px rgba(0,0,0,0.25);
  }
  .piece svg.art { position: absolute; inset: 0; width: 100%; height: 100%; }
  .brand { position: absolute; display: flex; align-items: center; gap: 5px; }
  .brand-dot { width: 12px; height: 12px; border-radius: 50%; background: var(--brand-blue); flex: none; }
  .brand-name { font-size: 6.5px; font-weight: 700; color: var(--brand-blue-deep); letter-spacing: .3px; text-transform: uppercase; line-height: 1.1; }
  .brand-tagline { font-size: 4px; color: var(--ink-soft); }
  .contact { position: absolute; text-align: left; font-size: 5px; line-height: 1.45; color: var(--ink); }
  .web { position: absolute; font-size: 5.5px; color: var(--accent-orange); font-weight: 600; }

  .letterhead { left: 233px; top: 34px; width: 408px; height: 585px; }
  .letterhead .brand { left: 38px; top: 36px; }
  .letterhead .contact { left: 296px; top: 32px; }
  .letterhead .web { right: 26px; bottom: 40px; }

  .business-card { left: 29px; top: 305px; width: 168px; height: 110px; }
  .business-card .card-name { position: absolute; left: 8px; top: 9px; font-size: 6px; font-weight: 700; color: var(--accent-orange); }
  .business-card .card-title { position: absolute; left: 8px; top: 17px; font-size: 4px; color: var(--ink-soft); }
  .business-card .contact { left: 8px; top: 60px; font-size: 4px; }

  .envelope-back { left: 677px; top: 79px; width: 494px; height: 216px; }

  .envelope-front { left: 677px; top: 331px; width: 494px; height: 245px; }
  .envelope-front .brand { left: 60px; top: 28px; }
  .envelope-front .contact { left: 380px; top: 26px; }
  .envelope-front .web { right: 22px; bottom: 30px; }
</style>
</head>
<body>

<section class="piece letterhead" aria-label="Letterhead">
  <svg class="art" viewBox="0 0 408 585" preserveAspectRatio="none" aria-hidden="true">
    <defs>
      <linearGradient id="lh-blue" x1="0" y1="0" x2="1" y2="1">
        <stop offset="0" stop-color="#5d9bd8"/>
        <stop offset=".6" stop-color="#2a6db5"/>
        <stop offset="1" stop-color="#1b4f8f"/>
      </linearGradient>
    </defs>
    <path d="M0,110 C55,210 70,400 210,585 L0,585 Z" fill="url(#lh-blue)"/>
    <path d="M0,100 C70,210 90,400 232,585" fill="none" stroke="#f0962a" stroke-width="4"/>
    <path d="M0,145 C40,240 50,420 150,585 L0,585 Z" fill="#1b4f8f" opacity=".35"/>
  </svg>
  <div class="brand">
    <span class="brand-dot"></span>
    <div>
      <div class="brand-name">Kinward Harbor Center</div>
      <div class="brand-tagline">Strengthening families in our community</div>
    </div>
  </div>
  <div class="contact">
    P: 973 555 0142<br>
    F: 973 555 0143<br>
    marisol.thackery@alderlanehub.org<br>
    48 Alder Lane Morristown, NJ 07931
  </div>
  <div class="web">www.alderlanehub.org</div>
</section>

<section class="piece business-card" aria-label="Business card">
  <svg class="art" viewBox="0 0 168 110" preserveAspectRatio="none" aria-hidden="true">
    <defs>
      <linearGradient id="bc-blue" x1="0" y1="0" x2="1" y2="1">
        <stop offset="0" stop-color="#5d9bd8"/>
        <stop offset="1" stop-color="#1b4f8f"/>
      </linearGradient>
    </defs>
    <path d="M0,0 H168 V8 Q84,26 0,8 Z" fill="url(#bc-blue)" opacity=".0"/>
    <path d="M168,0 V110 H88 C130,92 150,55 138,0 Z" fill="url(#bc-blue)"/>
    <path d="M132,0 C144,55 124,92 80,110" fill="none" stroke="#f0962a" stroke-width="2.5"/>
  </svg>
  <div class="card-name">Marisol Thackery</div>
  <div class="card-title">Executive Director</div>
  <div class="contact">
    www.alderlanehub.org<br>
    P: 973 555 0142<br>
    marisol.thackery@alderlanehub.org<br>
    48 Alder Lane Morristown, NJ 07931
  </div>
</section>

<section class="piece envelope-back" aria-label="Envelope back">
  <svg class="art" viewBox="0 0 494 216" preserveAspectRatio="none" aria-hidden="true">
    <defs>
      <radialGradient id="flap-blue" cx=".5" cy=".45" r=".65">
        <stop offset="0" stop-color="#5d9bd8"/>
        <stop offset=".55" stop-color="#2a6db5"/>
        <stop offset="1" stop-color="#1b4f8f"/>
      </radialGradient>
    </defs>
    <path d="M0,0 H494 V150 Q480,168 440,170 H54 Q14,168 0,150 Z" fill="url(#flap-blue)"/>
  </svg>
</section>

<section class="piece envelope-front" aria-label="Envelope front">
  <svg class="art" viewBox="0 0 494 245" preserveAspectRatio="none" aria-hidden="true">
    <defs>
      <linearGradient id="ef-blue" x1="0" y1="0" x2="1" y2="1">
        <stop offset="0" stop-color="#5d9bd8"/>
        <stop offset=".6" stop-color="#2a6db5"/>
        <stop offset="1" stop-color="#1b4f8f"/>
      </linearGradient>
    </defs>
    <path d="M0,0 H30 C10,90 50,190 140,245 H0 Z" fill="url(#ef-blue)"/>
    <path d="M38,0 C18,90 58,190 156,245" fill="none" stroke="#f0962a" stroke-width="3.5"/>
  </svg>
  <div class="brand">
    <span class="brand-dot"></span>
    <div>
      <div class="brand-name">Kinward Harbor Center</div>
      <div class="brand-tagline">Strengthening families in our community</div>
    </div>
  </div>
  <div class="contact">
    P: 973 555 0142<br>
    F: 973 555 0143<br>
    marisol.thackery@alderlanehub.org<br>
    48 Alder Lane Morristown, NJ 07931
  </div>
  <div class="web">www.alderlanehub.org</div>
</section>

</body>
</html>
```